shutter business card and postcard design

Custom Interior and Exterior Shutters manufactured In Houston Texas Made in USA we offer fast delivery lifetime warranty
Dean Whitfield owner has been manufacturing shutters in houston for over 44 years
nedd to use one of the pictures provided and add company name phone number on face Louver Loft (281)555-0187
back side
louver loft
8217 calloway ln.
houston, texas 77099
email louverloft@examplemail.test
website louverlofthouston.test

Industry/Entity Type

Business

```html
<!DOCTYPE html>
<html lang="en">
<head>
<meta charset="utf-8">
<title>Louver Loft – Business Card</title>
<link rel="stylesheet" href="https://fonts.googleapis.com/css2?family=Source+Sans+3:wght@400;600;700&display=swap">
<style>
  :root {
    --backdrop: #ecebe8;
    --card-white: #ffffff;
    --stone: #bdb8b1;
    --umber: #5f4c31;
    --tagline-grey: #b1aca5;
    --white: #ffffff;
  }
  * { margin: 0; padding: 0; box-sizing: border-box; }
  html, body {
    width: 1019px;
    height: 1200px;
    overflow: hidden;
    background: var(--backdrop);
    font-family: "Source Sans 3", "Myriad Pro", sans-serif;
  }
  .canvas { position: relative; width: 1019px; height: 1200px; }

  .card {
    position: absolute;
    width: 791px;
    height: 464px;
    overflow: hidden;
  }

  /* Front */
  .card--front { left: 55px; top: 64px; background: var(--card-white); }
  .front-brand {
    position: absolute;
    left: 185px;
    top: 244px;
  }
  .front-brand__name {
    font-size: 60px;
    font-weight: 700;
    color: var(--umber);
    line-height: 1;
    letter-spacing: 0.2px;
  }
  .front-brand__tagline {
    margin-top: 6px;
    font-size: 25px;
    font-weight: 400;
    color: var(--tagline-grey);
    line-height: 1;
  }

  .web-band {
    position: absolute;
    left: 0; bottom: 0;
    width: 100%;
    height: 45px;
    display: flex;
    align-items: center;
    justify-content: center;
    font-size: 23px;
    font-weight: 600;
  }
  .card--front .web-band { background: var(--stone); color: var(--white); }

  /* Back */
  .card--back { left: 133px; top: 615px; background: var(--stone); }
  .card--back .web-band { background: var(--card-white); color: var(--umber); }

  .back-brand { position: absolute; left: 38px; top: 175px; }
  .back-brand__name {
    font-size: 46px;
    font-weight: 700;
    color: var(--white);
    line-height: 1;
  }
  .back-brand__tagline {
    margin-top: 4px;
    font-size: 17px;
    font-weight: 600;
    color: var(--umber);
    line-height: 1;
  }

  .divider {
    position: absolute;
    left: 388px;
    top: 69px;
    width: 2px;
    height: 300px;
    background: var(--white);
  }

  .contact { position: absolute; left: 435px; top: 129px; color: var(--umber); }
  .contact__name { font-size: 26px; font-weight: 700; line-height: 1; margin-bottom: 20px; }
  .contact__row {
    display: flex;
    align-items: flex-start;
    gap: 24px;
    font-size: 23px;
    font-weight: 400;
    line-height: 31px;
    margin-bottom: 11px;
  }
  .contact__icon { flex: 0 0 22px; width: 22px; height: 22px; margin-top: 5px; }
</style>
</head>
<body>
<main class="canvas">

  <section class="card card--front" aria-label="Card front">
    <div class="front-brand">
      <h1 class="front-brand__name">Louver Loft</h1>
      <p class="front-brand__tagline">Houston’s Makers of Plantation Shutters</p>
    </div>
    <div class="web-band">www.louverlofthouston.test</div>
  </section>

  <section class="card card--back" aria-label="Card back">
    <div class="back-brand">
      <h2 class="back-brand__name">Louver Loft</h2>
      <p class="back-brand__tagline">Houston’s Makers of Plantation Shutters</p>
    </div>

    <div class="divider"></div>

    <div class="contact">
      <p class="contact__name">Dean Whitfield</p>

      <div class="contact__row">
        <svg class="contact__icon" viewBox="0 0 22 22" aria-hidden="true">
          <rect width="22" height="22" rx="4" fill="#fff"/>
          <path d="M7 5.5l2.2 2.6-1.2 1.6c.8 1.7 2 2.9 3.6 3.7l1.6-1.2 2.6 2.2-1.3 2c-4.6-.4-8.4-4.2-8.8-8.8z" fill="#5f4c31"/>
        </svg>
        <span>281-555-0187</span>
      </div>

      <div class="contact__row">
        <svg class="contact__icon" viewBox="0 0 22 22" aria-hidden="true">
          <rect width="22" height="22" rx="4" fill="#fff"/>
          <path d="M5 9.5l6-4 6 4v7H5z" fill="none" stroke="#5f4c31" stroke-width="1.6" stroke-linejoin="round"/>
          <path d="M5 9.5l6 4 6-4" fill="none" stroke="#5f4c31" stroke-width="1.6" stroke-linejoin="round"/>
        </svg>
        <span>louverloft@examplemail.test</span>
      </div>

      <div class="contact__row">
        <svg class="contact__icon" viewBox="0 0 22 22" aria-hidden="true">
          <rect width="22" height="22" rx="4" fill="#fff"/>
          <path d="M11 4.5a4.5 4.5 0 0 1 4.5 4.5c0 3.2-4.5 8.5-4.5 8.5S6.5 12.2 6.5 9A4.5 4.5 0 0 1 11 4.5z" fill="#5f4c31"/>
          <circle cx="11" cy="9" r="1.7" fill="#fff"/>
        </svg>
        <span>8217 calloway ln.<br>houston, texas 77099</span>
      </div>
    </div>

    <div class="web-band">www.louverlofthouston.test</div>
  </section>

</main>
</body>
</html>
```